Harborline Energy - needs a business card

Harborline Energy is a U.S. based diesel sourcing and distribution company that supports American oil & gas fields through providing quality product and consistent services.

Target Market(s)

Oil and Gas

Contact Information for Business Card

The background of the card must be white to ensure the logo pops.

Font styles to use
Serif
Sans Serif

Colors

Designer to choose colors to be used in the design.

Requirements
Must have
• Front of Card: Tag line: Harborline Energy, Powering America's Oil & Gas fields.
• Not sure if you guys do this part but just in case...
• Dale Menschow
• Owner/CEO
• C:555.318.4076
• E:Dmenschow@harborlineenergy.example
• W:Harborlineenergy.example
• Locations: Servicing the Powder River, DJ basin and Bakken formations.
• Back of Card: " Frac fueling is what we do. We understand how important diesel fuel is to your operation, which is why our main service line is Frac fueling. We assure our supply and stand by our service"

```html
<!DOCTYPE html>
<html lang="en">
<head>
<meta charset="utf-8">
<title>Harborline Energy – Business Card</title>
<link rel="stylesheet" href="https://fonts.googleapis.com/css2?family=Source+Sans+3:wght@400;600;700&display=swap">
<style>
  :root {
    --navy: #1f2f6b;
    --red: #e21d26;
    --red-deep: #8e1020;
    --white: #ffffff;
    --ghost: #e6e4ea;
    --ghost-warm: #f1e4dc;
    --backdrop: #232323;
  }
  * { margin: 0; padding: 0; box-sizing: border-box; }
  html, body { width: 1200px; height: 900px; overflow: hidden; }
  body {
    background: var(--backdrop);
    font-family: "Source Sans 3", sans-serif;
    position: relative;
  }
  .card {
    position: absolute;
    width: 560px;
    height: 320px;
    background: var(--white);
    overflow: hidden;
    box-shadow: 0 14px 30px rgba(0,0,0,.45);
  }
  .card--front { left: 70px; top: 90px; }
  .card--back { left: 570px; top: 490px; }
  .card__band { position: absolute; inset: 0; width: 100%; height: 100%; }
  .card__ghost-mark {
    position: absolute;
    right: -30px; top: -40px;
    width: 230px; height: 230px;
    border-radius: 50%;
    background: radial-gradient(circle at 40% 45%, var(--ghost-warm), var(--ghost) 70%);
    opacity: .75;
  }
  .brand {
    display: flex; align-items: center; gap: 8px;
    color: var(--navy);
    font-weight: 700;
    font-size: 28px;
    letter-spacing: .5px;
  }
  .brand__dot {
    width: 16px; height: 16px; border-radius: 50%;
    background: var(--red);
  }
  /* front */
  .front__identity {
    position: absolute; left: 40px; top: 78px; width: 220px;
    display: flex; flex-direction: column; align-items: center; text-align: center;
  }
  .front__identity .brand { font-size: 25px; }
  .tagline {
    margin-top: 12px;
    color: var(--navy);
    font-size: 15px;
    line-height: 1.3;
  }
  .front__divider {
    position: absolute; left: 272px; top: 48px;
    width: 2px; height: 140px; background: var(--navy);
  }
  .contact { position: absolute; left: 292px; top: 40px; width: 260px; }
  .contact__name { color: var(--red); font-weight: 700; font-size: 24px; line-height: 1; }
  .contact__role {
    display: inline-block; margin-top: 3px; padding-bottom: 3px;
    color: var(--navy); font-weight: 600; font-size: 17px;
    border-bottom: 3px solid var(--navy);
  }
  .contact__lines {
    list-style: none; margin-top: 16px;
    color: var(--navy); font-size: 12.5px; line-height: 1.45;
  }
  /* back */
  .back__identity {
    position: absolute; left: 0; right: 0; top: 70px;
    display: flex; justify-content: center;
  }
  .back__quote {
    position: absolute; left: 60px; right: 60px; top: 128px;
    color: var(--navy); font-size: 14px; line-height: 1.4; text-align: center;
  }
</style>
</head>
<body>

<section class="card card--front" aria-label="Business card front">
  <svg class="card__band" viewBox="0 0 560 320" preserveAspectRatio="none" aria-hidden="true">
    <defs>
      <linearGradient id="frontFold" x1="0" y1="1" x2="1" y2="0">
        <stop offset="0" stop-color="var(--red-deep)"/>
        <stop offset="1" stop-color="var(--red)"/>
      </linearGradient>
    </defs>
    <polygon points="0,320 0,240 240,228 560,120 560,320" fill="var(--red)"/>
    <polygon points="140,320 240,228 420,168" fill="url(#frontFold)"/>
  </svg>
  <div class="card__ghost-mark" role="img" aria-label="Faint large brand symbol as background decoration"></div>

  <div class="front__identity">
    <div class="brand"><span class="brand__dot"></span>Harborline Energy</div>
    <p class="tagline">Harborline Energy,<br>Powering America's Oil &amp; Gas fields.</p>
  </div>

  <div class="front__divider"></div>

  <div class="contact">
    <h1 class="contact__name">Dale Menschow</h1>
    <p class="contact__role">Owner/CEO</p>
    <ul class="contact__lines">
      <li>C: 555.318.4076</li>
      <li>E: Dmenschow@harborlineenergy.example</li>
      <li>W: Harborlineenergy.example</li>
      <li>Locations: Servicing the Powder River,</li>
      <li>DJ basin and Bakken formations</li>
    </ul>
  </div>
</section>

<section class="card card--back" aria-label="Business card back">
  <svg class="card__band" viewBox="0 0 560 320" preserveAspectRatio="none" aria-hidden="true">
    <defs>
      <linearGradient id="backFold" x1="0" y1="1" x2="1" y2="0">
        <stop offset="0" stop-color="var(--red-deep)"/>
        <stop offset="1" stop-color="var(--red)"/>
      </linearGradient>
    </defs>
    <polygon points="0,320 0,262 250,250 560,130 560,320" fill="var(--red)"/>
    <polygon points="150,320 250,250 430,182" fill="url(#backFold)"/>
  </svg>
  <div class="card__ghost-mark" role="img" aria-label="Faint large brand symbol as background decoration"></div>

  <div class="back__identity">
    <div class="brand"><span class="brand__dot"></span>Harborline Energy</div>
  </div>

  <p class="back__quote">"Frac fueling is what we do. We understand how important diesel fuel is to your operation, which is why our main service line is Frac fueling. We assure our supply and stand by our service"</p>
</section>

</body>
</html>
```